Website Landing Page for Brightfall Systems

Create a custom designed website landing page for our business. Looking for a professional upscale design that incorporates our logo and logo colors into the theme. I want a standard fixed frame website, not a constant scrolling format that seems to be the trend. To start with I'm looking for more of the graphic design part, maybe a concept or theme, I don't expect to see a finished project. Not interested in generic templates or layouts.

The name of our company is Brightfall Systems and I've attached our logo below. I'd like to have the web page have the same look and feel of our logo, as well as the colors. Our company, Brightfall Systems does system design, installation, and programming, of residential and commercial Audio/Video and Automation systems. We do home theaters, lighting and building automation, video conferencing systems, security camera installations, conference rooms, projectors, distributed audio systems, and similar Technology projects. This will be a professional services/informational website. We will not sell products on this website. This website will be used to advertise our company and communicate our services to prospective customers. Having a well designed, professional and clean website is one way we want to distinguish our company from the competition.

Here are some examples of what I consider a professional well designed website
http://www.qorlamstudio.com/Work/

Last year we had our tradlo store designed (with PixelMarket) and I'm really happy with the way it turned out. You can see it at www.HolvenGearDepot.com I consider this to be a great design and looking for the same level of quality with this new website. However, do not copy or use any part of this design in this new project. This tradlo store is completely separate from our other company Brightfall Systems. I only mention this tradlo store an an example of good work.

Reason: Still going through designs.

Reason: Still working on project and have not had time to review all designs and request revisions.

Reason: Sill going through designs and requesting revisions

Reason: still going through all the submissions we received.

Target Market(s)

People interested in Audio/Video, home theaters, home automation. We do sales, system design, and programming. We typically work on larger projects with both residential and commercial customers.

Industry/Entity Type

Business

Number of Pages Required

1 page

Requirements
Must have
• Great design elements. Please use a white background. I think white goes well with our logo colors.

```html
<!DOCTYPE html>
<html lang="en">
<head>
<meta charset="utf-8">
<title>Brightfall Systems — Landing Page</title>
<link href="https://fonts.googleapis.com/css2?family=Montserrat:wght@400;500;600;700&family=Nunito:wght@700;800;900&display=swap" rel="stylesheet">
<style>
  :root{
    --stage:#ececec;
    --sky-1:#45c4ea;
    --sky-2:#2f86d2;
    --green-1:#9ccd3a;
    --green-2:#4fb848;
    --blue:#2a9fe0;
    --blue-deep:#1f6fb8;
    --white:#ffffff;
    --ink:#2b2b2b;
    --muted:#9a9a9a;
    --city-1:#5f6f80;
    --city-2:#3a4a3c;
  }
  *{box-sizing:border-box;margin:0;padding:0}
  html,body{width:1200px;height:1200px;overflow:hidden;background:var(--stage)}
  body{font-family:"Montserrat",sans-serif;position:relative}
  .page{
    position:absolute;left:190px;top:0;width:883px;height:1293px;
    transform:scale(0.928);transform-origin:0 0;background:var(--white);overflow:hidden;
  }
  .layer{position:absolute;left:0;top:0}
  .hero-photo{position:absolute;left:0;top:0;width:883px;height:450px;
    background:linear-gradient(160deg,var(--sky-1) 0%,#3aa6e2 45%,var(--sky-2) 100%)}
  .city-photo{position:absolute;left:0;top:760px;width:883px;height:309px;
    background:linear-gradient(180deg,#7c8c9c 0%,var(--city-1) 45%,var(--city-2) 100%)}
  .city-photo::after{content:"";position:absolute;inset:0;background:rgba(20,30,40,.25)}

  /* header */
  .brand{position:absolute;left:110px;top:21px;display:flex;align-items:center;gap:12px}
  .brand-dot{width:52px;height:52px;border-radius:50%;border:4px solid var(--white)}
  .brand-name{font-family:"Nunito",sans-serif;font-weight:800;color:var(--white);font-size:15px;line-height:16px;letter-spacing:1px;text-transform:uppercase}
  .topbar{position:absolute;left:542px;top:36px;display:flex;align-items:center;gap:10px;color:var(--white);font-size:12px;font-weight:500}
  .topbar .phone{display:flex;align-items:center;gap:7px;margin-left:14px}
  .btn{display:inline-block;border-radius:14px;font-weight:700;text-align:center}
  .btn-top{background:var(--green-1);color:var(--white);font-size:9px;padding:7px 14px;margin-left:2px}

  .hero-copy{position:absolute;left:0;width:883px;top:108px;text-align:center;color:var(--white);font-family:"Nunito",sans-serif}
  .hero-copy h1{font-size:27px;font-weight:900;letter-spacing:.3px}
  .hero-copy p{font-size:19px;font-weight:800;margin-top:6px}
  .btn-hero{background:var(--white);color:var(--blue-deep);font-family:"Montserrat",sans-serif;font-size:12px;padding:8px 18px;margin-top:15px;border-radius:16px}

  .perk{position:absolute;top:268px;width:90px;margin-left:-45px;text-align:center;color:var(--white);font-size:8.5px;font-weight:700;line-height:10px}
  .perk svg{display:block;margin:0 auto 4px}

  /* services */
  .services-title{position:absolute;left:0;width:883px;top:500px;text-align:center}
  .services-title .rule{display:block;width:70px;height:3px;border-radius:2px;background:var(--green-2);margin:0 auto}
  .services-title h2{font-family:"Nunito",sans-serif;font-weight:900;font-size:24px;color:var(--green-2);margin-top:12px}
  .service{position:absolute;border-radius:50%;overflow:hidden;display:flex;flex-direction:column;align-items:center;justify-content:center;color:var(--white);text-align:center;font-weight:700;font-size:10px;line-height:12px;text-transform:uppercase}
  .service .label{position:relative;margin-top:-16px}
  .service-photo{background:radial-gradient(circle at 50% 35%,#c9a47a 0%,#7e5a3e 55%,#3e2e22 100%)}
  .service-photo.dark{background:radial-gradient(circle at 50% 30%,#b07a5a 0%,#6a3a28 55%,#2c1c16 100%)}
  .service-feature{background:linear-gradient(180deg,var(--green-1) 0%,var(--green-2) 100%);font-size:11px;line-height:14px}
  .service-feature .more{display:block;text-transform:none;font-weight:500;font-size:9.5px;margin-top:8px;opacity:.9}

  .dots{position:absolute;left:456px;top:756px;display:flex;gap:6px}
  .dots span{width:9px;height:9px;border-radius:50%;background:#cfcfcf}
  .dots span:first-child{background:var(--blue)}

  .cta{position:absolute;left:0;width:883px;top:926px;text-align:center;color:var(--white)}
  .cta h3{font-size:18.5px;font-weight:600;letter-spacing:-.3px}
  .cta p{font-size:13px;font-weight:600;margin-top:14px}
  .btn-cta{background:var(--green-1);color:#1d3a10;font-size:9.5px;padding:8px 18px;margin-top:11px;border-radius:14px}

  /* footer */
  .footer{position:absolute;left:0;top:1069px;width:883px;height:224px;text-align:center}
  .footer-dot{width:50px;height:50px;border-radius:50%;border:4px solid var(--blue);margin:27px auto 0}
  .footer-name{font-family:"Nunito",sans-serif;font-weight:800;font-size:15px;letter-spacing:1px;color:var(--blue);margin-top:12px;text-transform:uppercase}
  .social{display:flex;justify-content:center;gap:7px;margin-top:17px}
  .social span{width:18px;height:18px;border-radius:50%;background:var(--blue-deep)}
  .legal{width:440px;margin:15px auto 0;font-size:6.5px;line-height:9px;color:var(--muted)}
  .copy{font-size:6px;color:var(--ink);margin-top:13px;font-weight:600}
</style>
</head>
<body>
<div class="page">

  <div class="hero-photo" role="img" aria-label="Photo of a large auditorium with rows of seats under a blue tint"></div>
  <div class="city-photo" role="img" aria-label="Photo of a city skyline with trees under a cloudy sky"></div>

  <svg class="layer" width="883" height="1293" viewBox="0 0 883 1293" aria-hidden="true">
    <defs>
      <linearGradient id="greenBand" x1="0" y1="0" x2="1" y2="0">
        <stop offset="0" stop-color="#4fb848"/>
        <stop offset=".5" stop-color="#9ccd3a"/>
        <stop offset="1" stop-color="#4fb848"/>
      </linearGradient>
      <filter id="soft" x="-10%" y="-20%" width="120%" height="160%">
        <feDropShadow dx="0" dy="4" stdDeviation="6" flood-color="#000" flood-opacity=".18"/>
      </filter>
    </defs>
    <!-- hero edge: one gentle curve with a green band -->
    <path fill="#ffffff" d="M-10 372 Q441.5 462 893 372 L893 460 L-10 460 Z"/>
    <path fill="none" stroke="url(#greenBand)" stroke-width="16" d="M-10 372 Q441.5 462 893 372"/>

    <!-- lower edge: white curve over the city photo -->
    <path fill="#ffffff" filter="url(#soft)" d="M-10 740 L893 740 L893 800 Q441.5 880 -10 800 Z"/>
  </svg>

  <header>
    <div class="brand">
      <span class="brand-dot"></span>
      <span class="brand-name">Brightfall<br>Systems</span>
    </div>
    <div class="topbar">
      <svg width="13" height="13" viewBox="0 0 13 13" aria-label="Search"><circle cx="5.5" cy="5.5" r="4" fill="none" stroke="#fff" stroke-width="1.6"/><path d="M8.5 8.5 L12 12" stroke="#fff" stroke-width="1.6" stroke-linecap="round"/></svg>
      <span class="phone">
        <svg width="12" height="12" viewBox="0 0 12 12" aria-hidden="true"><path d="M2.5 1 L4.5 1 L5.3 3.6 L4 4.6 C4.7 6 6 7.3 7.4 8 L8.4 6.7 L11 7.5 L11 9.5 C11 10.4 10.3 11 9.5 11 C5 11 1 7 1 2.5 C1 1.7 1.6 1 2.5 1 Z" fill="#9ccd3a"/></svg>
        888.555.0142
      </span>
      <span class="btn btn-top">Contact us</span>
    </div>
  </header>

  <section class="hero-copy">
    <h1>Welcome to Brightfall Systems</h1>
    <p>We Provide Minimum 1-year Warranty</p>
    <span class="btn btn-hero">Contact us</span>
  </section>

  <div class="perk" style="left:180px">
    <svg width="52" height="52" viewBox="0 0 52 52" aria-hidden="true"><circle cx="26" cy="26" r="23" fill="none" stroke="#fff" stroke-width="3"/><rect x="15" y="16" width="22" height="18" rx="2" fill="none" stroke="#fff" stroke-width="2"/><circle cx="26" cy="24" r="4" fill="none" stroke="#fff" stroke-width="2"/><path d="M23 28 L22 33 L26 31 L30 33 L29 28" fill="#fff"/></svg>
    Authorized<br>Dealer
  </div>
  <div class="perk" style="left:374px">
    <svg width="52" height="52" viewBox="0 0 52 52" aria-hidden="true"><circle cx="26" cy="26" r="23" fill="none" stroke="#fff" stroke-width="3"/><circle cx="26" cy="26" r="12" fill="none" stroke="#fff" stroke-width="4" stroke-dasharray="4 3"/><circle cx="26" cy="26" r="8" fill="#fff"/><text x="26" y="30" text-anchor="middle" font-family="Montserrat,sans-serif" font-weight="700" font-size="11" fill="#3aa6e2">$</text></svg>
    Extreme<br>Low Prices
  </div>
  <div class="perk" style="left:575px">
    <svg width="52" height="52" viewBox="0 0 52 52" aria-hidden="true"><circle cx="26" cy="26" r="23" fill="none" stroke="#fff" stroke-width="3"/><circle cx="26" cy="26" r="12" fill="none" stroke="#fff" stroke-width="4" stroke-dasharray="4 3"/><path d="M20 32 L30 22" stroke="#fff" stroke-width="3" stroke-linecap="round"/><circle cx="31" cy="21" r="3" fill="none" stroke="#fff" stroke-width="2"/></svg>
    Free Tech<br>Support
  </div>
  <div class="perk" style="left:778px">
    <svg width="52" height="52" viewBox="0 0 52 52" aria-hidden="true"><circle cx="26" cy="26" r="23" fill="none" stroke="#fff" stroke-width="3"/><circle cx="22" cy="29" r="7" fill="none" stroke="#fff" stroke-width="4" stroke-dasharray="3 2"/><circle cx="32" cy="19" r="5" fill="none" stroke="#fff" stroke-width="3" stroke-dasharray="2.5 2"/></svg>
    30-Day<br>Returns
  </div>

  <section class="services-title">
    <span class="rule"></span>
    <h2>Our Services</h2>
  </section>

  <div class="service service-photo" style="left:111px;top:575px;width:140px;height:140px" role="img" aria-label="Photo of a home theater living room">
    <span class="label">Home<br>Theaters</span>
  </div>
  <div class="service service-feature" style="left:273px;top:558px;width:164px;height:164px">
    <span class="label">Lighting<br>and Building<br>Automation<span class="more">Read More</span></span>
  </div>
  <div class="service service-photo dark" style="left:457px;top:574px;width:142px;height:142px" role="img" aria-label="Photo of a conference room with a long table and screen">
    <span class="label">Video Conferencing<br>Systems</span>
  </div>
  <div class="service service-photo" style="left:630px;top:574px;width:142px;height:142px" role="img" aria-label="Photo of a furnished interior with security cameras">
    <span class="label">Security Camera<br>Installations</span>
  </div>

  <div class="dots"><span></span><span></span><span></span></div>

  <section class="cta">
    <h3>If you don't see what you're looking for, Contact Us!</h3>
    <p>Or Call Us Today: (281) 555-0190</p>
    <span class="btn btn-cta">CONTACT US</span>
  </section>

  <footer class="footer">
    <div class="footer-dot"></div>
    <div class="footer-name">Brightfall Systems</div>
    <div class="social"><span></span><span></span><span></span><span></span></div>
    <p class="legal">All brand names, model numbers and product details are shown only to describe the items we install and do not imply any endorsement. Product names and marks belong to their respective owners.</p>
    <p class="copy">Copyright © 2017 Brightfall Systems. All Rights Reserved.</p>
  </footer>

</div>
</body>
</html>
```